Zielgruppe
Wir sind gerade dabei ein Buch zum Thema 'Konzentrationstraining für Kinder' zu erstellen und brauchen jetzt ein passendes Cover dazu. Bei der Zielgruppe handelt es sich hauptsächlich um Mütter die Lösungen für die Konzentrationsprobleme Ihrer Kinder im Grundschulalter suchen. Die Kinder haben diese Probleme hauptsächlich in der Schule. Das Buch beschreibt hauptsächlich Konzentrationsübungen und -spiele für die Kinder aber auch allgemeine Tipps zur Konzentrationssteigerung wie z.B. Ernährung, Umfeld usw.
Aufgabenstellung
Ein Comic-Stil beim Cover kommt offensichtlich beim Kunden gut an (Konkurrenzanalyse)
Titel, Untertitel und Autorenname müssen auf dem Cover stehen.
Der Titel des Buches lautet: Die stille Insel - Konzentrationstraining für Kinder in der Praxis: Die 39 besten Übungen für nachhaltig mehr Aufmerksamkeit und Konzentration in der Schule und im Alltag
Autor: Henrike Albmann
Das Cover wird in 3 verschiedenen Versionen benötigt: Taschenbuch: 5,25 x 8 inch 2. Hardcover: 6 x 9 inch 3. EBook: 2,560 x 1,600 pixel.

```html
<!DOCTYPE html>
<html lang="de">
<head>
<meta charset="utf-8">
<title>Die stille Insel – Cover</title>
<link rel="stylesheet" href="https://fonts.googleapis.com/css2?family=Fira+Sans+Condensed:wght@600&family=Varela+Round&family=Nunito:ital,wght@0,600;1,500&display=swap">
<style>
  :root {
    --plum: #71306a;
    --taupe: #766b69;
    --paper: #ffffff;
    --tone-warm: #ee8a48;
    --tone-green: #5bae60;
    --tone-teal: #3fb0b8;
    --tone-berry: #b0407e;
  }
  html, body {
    margin: 0;
    padding: 0;
    width: 837px;
    height: 1200px;
    overflow: hidden;
    background: var(--paper);
  }
  .cover {
    position: relative;
    width: 837px;
    height: 1200px;
    background: var(--paper);
  }
  .author {
    position: absolute;
    right: 82px;
    top: 28px;
    margin: 0;
    font-family: "Varela Round", sans-serif;
    font-size: 35px;
    font-weight: 400;
    color: var(--taupe);
    letter-spacing: 0.5px;
  }
  .title {
    position: absolute;
    left: 68px;
    top: 66px;
    margin: 0;
    font-family: "Fira Sans Condensed", sans-serif;
    font-weight: 600;
    font-size: 94px;
    line-height: 1;
    letter-spacing: -3px;
    color: var(--plum);
  }
  .subtitle {
    position: absolute;
    left: 70px;
    top: 168px;
    margin: 0;
    font-family: "Nunito", sans-serif;
    font-weight: 600;
    color: var(--taupe);
    line-height: 1;
  }
  .subtitle .kicker {
    display: block;
    font-size: 37px;
    letter-spacing: 0.5px;
  }
  .subtitle .rest {
    display: block;
    font-size: 34px;
    margin-top: 3px;
  }
  .artwork {
    position: absolute;
    left: 78px;
    top: 298px;
    width: 735px;
    height: 688px;
  }
  .tagline {
    position: absolute;
    left: 70px;
    top: 1118px;
    margin: 0;
    font-family: "Nunito", sans-serif;
    font-style: italic;
    font-weight: 500;
    font-size: 24px;
    line-height: 1.2;
    color: var(--plum);
  }
</style>
</head>
<body>
<main class="cover">
  <p class="author">Henrike Albmann</p>
  <h1 class="title">Die stille Insel</h1>
  <h2 class="subtitle">
    <span class="kicker">KONZENTRATIONSTRAINING</span>
    <span class="rest">für Kinder in der Praxis</span>
  </h2>

  <svg class="artwork" viewBox="0 0 735 688" role="img" aria-label="Illustration: fröhliches Kind mit ausgebreiteten Armen vor bunten Farbflächen">
    <defs>
      <linearGradient id="tone-wash" x1="0" y1="0" x2="1" y2="1">
        <stop offset="0" stop-color="var(--tone-warm)"/>
        <stop offset="0.35" stop-color="var(--tone-green)"/>
        <stop offset="0.65" stop-color="var(--tone-teal)"/>
        <stop offset="1" stop-color="var(--tone-berry)"/>
      </linearGradient>
      <radialGradient id="soft-edge" cx="0.5" cy="0.5" r="0.5">
        <stop offset="0" stop-color="#fff" stop-opacity="1"/>
        <stop offset="0.75" stop-color="#fff" stop-opacity="0.9"/>
        <stop offset="1" stop-color="#fff" stop-opacity="0"/>
      </radialGradient>
      <mask id="fade">
        <rect width="735" height="688" fill="url(#soft-edge)"/>
      </mask>
    </defs>
    <rect class="artwork-fill" width="735" height="688" fill="url(#tone-wash)" opacity="0.85" mask="url(#fade)"/>
  </svg>

  <p class="tagline">Die 39 besten Übungen für nachhaltig mehr Aufmerksamkeit<br>und Konzentration in der Schule und im Alltag</p>
</main>
</body>
</html>
```